Orthodontist Needs Promotional Discount Postcard

5.5 x 8.5 Horizontal 2-Sided Postcard for mailing.
Images & Logo on both sides okay; must be free stock Images from legit sources only, or use attached images. See our website for information, CoveLineSmiles.com
Context to include:
New Patient Special $500 off Braces or Clear Aligners
Cannot be combined with any other discounts.
Major dental insurance plans and Vita-Plan accepted
Affordable payment options are available
Call to schedule your free consultation
Present this new patient offer to receive your discount.
Offer ends January 31, 2022.
805-419-2276 www. CoveLineSmiles.com
462 N. Marigold Street, Suite B, Ventura, CA 93001-5812
office@covelinesmiles.com

```html
<!DOCTYPE html>
<html lang="en">
<head>
<meta charset="utf-8">
<title>Cove Line Smiles – New Patient Postcard</title>
<link href="https://fonts.googleapis.com/css2?family=Poppins:wght@300;400;500;600;700&family=Montserrat:wght@600;700;800&display=swap" rel="stylesheet">
<style>
:root{
  --blue:#27a3dd;
  --blue-deep:#1f88c0;
  --navy:#1c5f86;
  --grey-dark:#5f6166;
  --grey-band:#6b6d72;
  --grey-bar:#e3e4e6;
  --ink:#3d3f44;
  --paper:#f6f7f8;
  --bg:#d9d9da;
  --white:#ffffff;
  --photo-line:#6ec7ef;
}
*{box-sizing:border-box;margin:0;padding:0}
html,body{width:750px;height:1200px;overflow:hidden;background:var(--bg);font-family:"Poppins",sans-serif;color:var(--ink)}
.card{position:absolute;left:25px;width:700px;height:453px;background:var(--paper);box-shadow:0 6px 18px rgba(0,0,0,.18);overflow:hidden}
.card--front{top:70px}
.card--back{top:640px}
.abs{position:absolute}

.brand{display:flex;align-items:center;gap:8px}
.brand__dot{width:30px;height:30px;border-radius:50%;background:var(--blue)}
.brand__name{font-weight:400;font-size:17px;color:var(--blue);letter-spacing:.5px;text-transform:uppercase}

.headline{left:32px;top:82px;font-family:"Montserrat",sans-serif;font-weight:800;font-size:26px;color:var(--grey-dark);letter-spacing:-.3px;white-space:nowrap}
.headline span{color:var(--blue)}

.offer{left:32px;top:133px;width:378px;height:72px;display:flex}
.offer__amount{width:198px;background:var(--blue);color:var(--white);display:flex;align-items:center;padding-left:14px;font-weight:600}
.offer__amount sup{font-size:18px;align-self:flex-start;margin-top:13px}
.offer__amount b{font-size:50px;font-weight:600;line-height:1}
.offer__amount i{font-style:normal;font-size:20px;margin-left:8px;border-bottom:2px solid var(--white);line-height:1.1}
.offer__items{flex:1;background:var(--blue-deep);color:var(--white);padding:13px 0 0 14px;font-size:13.5px;line-height:24px;font-weight:700;white-space:nowrap}
.offer__items span{font-weight:400}
.offer__items svg{width:14px;height:14px;vertical-align:-2px;margin-right:6px}
.notice{left:32px;top:205px;width:378px;height:22px;background:var(--grey-band);color:var(--white);font-size:11.5px;text-align:center;line-height:22px;text-transform:uppercase;white-space:nowrap}
.notice b{font-weight:700}

.checks{left:32px;top:240px;font-size:12px;font-weight:300;color:var(--ink);line-height:22px;list-style:none;white-space:nowrap}
.checks svg{width:14px;height:14px;vertical-align:-2px;margin-right:6px}

.cta{border-left:3px solid var(--blue);padding-left:8px;white-space:nowrap}
.cta__lead{font-size:12.5px;font-weight:500;text-transform:uppercase;color:var(--ink);line-height:15px}
.cta__main{font-family:"Montserrat",sans-serif;font-weight:800;color:var(--blue);font-size:20px;line-height:28px}
.cta__note{font-size:8px;color:var(--grey-dark)}
.cta--back .cta__main{font-size:18.5px}
.cta--back .cta__lead{font-size:12px}
.cta--back .cta__note{font-size:7.5px}
.ends{border-left:1px solid #c9cacc;padding-left:14px;text-align:center;font-size:12px;text-transform:uppercase;color:var(--ink);white-space:nowrap}
.ends__date{display:block;background:var(--blue);color:var(--white);font-size:11px;font-weight:600;text-transform:none;margin:2px 0}
.ends__year{display:block;font-size:16px;font-weight:300;border-bottom:2px solid var(--blue);letter-spacing:1px}

.contact-bar{left:0;top:392px;height:36px;background:var(--grey-bar);display:flex;align-items:center;padding-left:32px;gap:16px;white-space:nowrap}
.contact-bar__phone{font-family:"Montserrat",sans-serif;font-weight:700;font-size:17px;color:var(--grey-dark)}
.contact-bar__web{font-size:11px;font-weight:500;color:var(--grey-dark);letter-spacing:.5px}
.contact-bar svg{width:11px;height:11px;vertical-align:-1px;margin-right:3px}

.photo{background:linear-gradient(135deg,#e8a3a0 0%,#f6d6d2 35%,#ffffff 60%,#f3c2bd 85%,#d98e8d 100%)}
.accent{left:532px;top:20px;width:142px;height:150px;border-top:4px solid var(--photo-line);border-right:4px solid var(--photo-line)}
.strip{left:388px;top:327px;width:286px;height:101px;background:var(--navy);display:flex;gap:8px;padding:10px 10px}
.thumb{flex:1;border:2px solid #5ab8e6}

.consult{left:0;top:0;width:338px;height:178px;background:var(--blue);color:var(--white)}
.consult__title{position:absolute;left:32px;top:38px;font-size:13px;font-weight:600}
.consult__text{position:absolute;left:32px;top:62px;width:146px;font-size:8px;line-height:10.6px;text-align:justify}
.consult__portrait{position:absolute;left:217px;top:36px;width:92px;height:92px;border-radius:50%;border:3px solid var(--white);background:linear-gradient(180deg,#d8b878 0%,#7e95a8 55%,#34465e 100%)}
.consult__name{position:absolute;left:210px;top:133px;font-size:8.5px;font-weight:600;white-space:nowrap}
.consult__role{position:absolute;left:210px;top:144px;font-size:5.5px;opacity:.9}
.gallery{left:32px;top:198px;width:306px;height:94px;display:flex;gap:12px}
.gallery .thumb{border-color:var(--blue)}

.mailing{left:395px;top:40px}
.mailing .brand__dot{width:26px;height:26px}
.mailing .brand__name{font-size:13px}
.address{left:395px;top:84px;font-size:8px;line-height:11px;color:var(--ink)}
.stamp{left:600px;top:40px;width:65px;height:82px;border:1px solid #b9babd}
.line{left:395px;width:270px;height:1px;background:#c3c4c7}
</style>
</head>
<body>

<section class="card card--front">
  <div class="accent abs"></div>
  <div class="photo abs" style="left:388px;top:26px;width:286px;height:301px" role="img" aria-label="Close-up photo of a bright white smile with a dental mirror"></div>
  <div class="strip abs">
    <div class="thumb photo" role="img" aria-label="Photo of teeth with metal braces"></div>
    <div class="thumb photo" role="img" aria-label="Photo of a clear aligner being fitted"></div>
    <div class="thumb photo" role="img" aria-label="Photo of a smile with a dental mirror"></div>
  </div>

  <div class="brand abs" style="left:32px;top:26px"><span class="brand__dot"></span><span class="brand__name">Cove Line Smiles</span></div>
  <h1 class="headline abs">NEW PATIENT <span>SPECIAL</span></h1>
  <div class="offer abs">
    <div class="offer__amount"><sup>$</sup><b>500</b><i>OFF</i></div>
    <div class="offer__items">
      <div><svg viewBox="0 0 14 14"><rect x="1" y="3" width="12" height="8" rx="2" fill="none" stroke="#fff" stroke-width="1.4"/><line x1="1" y1="7" x2="13" y2="7" stroke="#fff" stroke-width="1.2"/></svg>BRACES <span>OR</span></div>
      <div><svg viewBox="0 0 14 14"><path d="M3 2c2-1 3 1 4 1s2-2 4-1c2 1 1 5 0 7l-1 4-2-4-1 4-1-4-2 4-1-4c-1-2-2-6 0-7z" fill="none" stroke="#fff" stroke-width="1.2"/></svg>CLEAR ALIGNERS</div>
    </div>
  </div>
  <div class="notice abs">Cannot be combined with any <b>other discounts</b></div>
  <ul class="checks abs">
    <li><svg viewBox="0 0 14 14"><rect x="1" y="1" width="12" height="12" rx="2" fill="none" stroke="#27a3dd" stroke-width="1.5"/><path d="M3.5 7l2.5 2.5 5-6" fill="none" stroke="#27a3dd" stroke-width="1.8"/></svg>Major dental insurance plans and Vita-Plan accepted</li>
    <li><svg viewBox="0 0 14 14"><rect x="1" y="1" width="12" height="12" rx="2" fill="none" stroke="#27a3dd" stroke-width="1.5"/><path d="M3.5 7l2.5 2.5 5-6" fill="none" stroke="#27a3dd" stroke-width="1.8"/></svg>Affordable payment options are available</li>
  </ul>
  <div class="cta abs" style="left:32px;top:318px">
    <p class="cta__lead">Call to schedule your</p>
    <p class="cta__main">Free Consultation</p>
    <p class="cta__note">Present this new patient offer to receive your discount.</p>
  </div>
  <div class="ends abs" style="left:274px;top:318px;width:92px">Offer ends<span class="ends__date">January 31</span><span class="ends__year">2022</span></div>
  <div class="contact-bar abs" style="width:380px">
    <span class="contact-bar__phone"><svg viewBox="0 0 12 12"><path d="M2 1l2.5 0 1 3-1.5 1c.7 1.5 1.5 2.3 3 3l1-1.5 3 1V10c0 .6-.5 1-1 1C5 11 1 7 1 2c0-.5.4-1 1-1z" fill="#27a3dd"/></svg>805-419-2276</span>
    <span class="contact-bar__web"><svg viewBox="0 0 12 12"><circle cx="6" cy="6" r="5" fill="#27a3dd"/></svg>www. covelinesmiles.com</span>
  </div>
</section>

<section class="card card--back">
  <div class="consult abs">
    <h2 class="consult__title">VIRTUAL CONSULT</h2>
    <p class="consult__text">Want to get an idea of what it will take to straighten your teeth and give you the gorgeous, confident smile you've always wanted? Schedule a free virtual consultation to find out everything you need to know about treatment including fees!</p>
    <div class="consult__portrait" role="img" aria-label="Portrait photo of the orthodontist"></div>
    <p class="consult__name">Daniel R Westover, DDS, MS</p>
    <p class="consult__role">Certified Orthodontic Specialist</p>
  </div>
  <div class="gallery abs">
    <div class="thumb photo" role="img" aria-label="Photo of teeth with metal braces"></div>
    <div class="thumb photo" role="img" aria-label="Photo of a clear aligner being fitted"></div>
    <div class="thumb photo" role="img" aria-label="Photo of a smile with a dental mirror"></div>
  </div>
  <div class="cta cta--back abs" style="left:32px;top:322px">
    <p class="cta__lead">Call to schedule your</p>
    <p class="cta__main">Free Consultation</p>
    <p class="cta__note">Present this new patient offer to receive your discount.</p>
  </div>
  <div class="ends abs" style="left:258px;top:322px;width:82px">Offer ends<span class="ends__date">January 31</span><span class="ends__year">2022</span></div>
  <div class="contact-bar abs" style="width:338px">
    <span class="contact-bar__phone" style="font-size:15px"><svg viewBox="0 0 12 12"><path d="M2 1l2.5 0 1 3-1.5 1c.7 1.5 1.5 2.3 3 3l1-1.5 3 1V10c0 .6-.5 1-1 1C5 11 1 7 1 2c0-.5.4-1 1-1z" fill="#27a3dd"/></svg>805-419-2276</span>
    <span class="contact-bar__web" style="font-size:10px"><svg viewBox="0 0 12 12"><circle cx="6" cy="6" r="5" fill="#27a3dd"/></svg>www. covelinesmiles.com</span>
  </div>
  <div class="brand mailing abs"><span class="brand__dot"></span><span class="brand__name">Cove Line Smiles</span></div>
  <p class="address abs">462 N. Marigold Street,<br>Suite B, Ventura, CA<br>93001-5812</p>
  <div class="stamp abs"></div>
  <div class="line abs" style="top:185px"></div>
  <div class="line abs" style="top:232px"></div>
  <div class="line abs" style="top:276px"></div>
  <div class="line abs" style="top:322px"></div>
</section>

</body>
</html>
```